lawn sign

we need a design for our organic mosquito spray service. should fit a 27in x 18in yard sign. Includes our company logo and a picture of a mosquito with a circle around it crossed out (example included).

It needs to be simple, easily readable and in clear resolution. Signs needs to include the text: "this lawn receives ORGANIC treatments for mosquitoes and chiggers. Instantly SAFE for people and pets".

Include our phone number and website "615-372-5160" "yardnestle.com"

our ideas are: organic = no pests (use example pic)
no chemicals used = safe
Updates

Project Deadline Extended
Reason: we have been too busy to look at all of the designs. we will look at them all in the next day. thank you for your efforts and creativity!

Industry/Entity Type

It Company

```html
<!DOCTYPE html>
<html lang="en">
<head>
<meta charset="utf-8">
<title>Yard Sign – Organic Mosquito Treatment</title>
<link href="https://fonts.googleapis.com/css2?family=Raleway:wght@200;300;400;600;700;800;900&display=swap" rel="stylesheet">
<style>
  :root {
    --page-bg: #e3e8ee;
    --sign-top: #6a88ad;
    --sign-bottom: #1c4075;
    --ink: #ffffff;
    --ink-soft: rgba(255,255,255,0.85);
    --divider: rgba(255,255,255,0.75);
    --icon-fill: rgba(255,255,255,0.18);
  }
  * { margin: 0; padding: 0; box-sizing: border-box; }
  html, body {
    width: 1200px; height: 1000px; overflow: hidden;
    background: var(--page-bg);
    font-family: "Raleway", sans-serif;
  }
  .yard-sign {
    position: absolute; left: 60px; top: 140px;
    width: 1080px; height: 720px;
    background: linear-gradient(180deg, var(--sign-top) 0%, var(--sign-bottom) 100%);
    display: flex; align-items: center;
    color: var(--ink);
  }
  .message {
    width: 620px; padding-left: 44px;
    line-height: 1.02;
  }
  .message span { display: block; white-space: nowrap; }
  .intro { font-weight: 200; font-size: 60px; }
  .organic { font-weight: 900; font-size: 112px; letter-spacing: 1px; }
  .treatments { font-weight: 800; font-size: 76px; }
  .pests { font-weight: 600; font-size: 67px; }
  .safe { font-weight: 400; font-size: 68px; margin-top: 4px; }
  .audience { font-weight: 200; font-size: 54px; }
  .divider {
    width: 2px; height: 600px; background: var(--divider);
    margin-left: 10px;
  }
  .brand-panel {
    flex: 1; height: 100%;
    display: flex; flex-direction: column; align-items: center; justify-content: center;
  }
  .brand-name { font-weight: 600; font-size: 44px; letter-spacing: 0.5px; }
  .no-pest-icon { margin-top: 50px; width: 230px; height: 230px; }
  .contact { margin-top: 60px; font-weight: 400; font-size: 18px; color: var(--ink-soft); }
</style>
</head>
<body>
  <main class="yard-sign">
    <section class="message">
      <span class="intro">this lawn receives</span>
      <span class="organic">ORGANIC</span>
      <span class="treatments">TREATMENTS</span>
      <span class="pests">for mosquitoes</span>
      <span class="pests">and chiggers.</span>
      <span class="safe">Instantly SAFE</span>
      <span class="audience">for people and pets</span>
    </section>
    <div class="divider"></div>
    <aside class="brand-panel">
      <div class="brand-name">yardnestle</div>
      <svg class="no-pest-icon" viewBox="0 0 230 230">
        <circle cx="115" cy="115" r="110" fill="none" stroke="#ffffff" stroke-width="2.5"/>
        <circle cx="115" cy="115" r="62" fill="var(--icon-fill)" role="img" aria-label="mosquito silhouette"/>
        <line x1="60" y1="200" x2="170" y2="30" stroke="#ffffff" stroke-width="2.5"/>
      </svg>
      <div class="contact">615-372-5160 • www.yardnestle.com</div>
    </aside>
  </main>
</body>
</html>
```